Brantley Lawn Care. The best in the biz

I run a lawn care service that offers full service mowing. 100% satisfaction guarantee. Fast, Friendly, quality service "I am your lawns best friend" I cut residential lawns. I offer a mow package that includes trimming, edging and clean up. Prices very from 20 dollars to 75. I want my logo to stand out. Free estimates

Target Market(s)

Home owners

Industry/Entity Type

Landscaping

Contact Information for Business Card

555-612-4470 tidymow47@quillmail.example Dexter. Brantley Lawn care

Colors
f37122
9bcb3c
cadf82

Requirements
Must have
• Company name.
• Phone number
• Email
• My services
• images
Nice to have
• A sun that is growing grass.
Should not have
• Incorrect information

```html
<!DOCTYPE html>
<html lang="en">
<head>
<meta charset="utf-8">
<title>Brantley Lawn Care – Business Card</title>
<link rel="stylesheet" href="https://fonts.googleapis.com/css2?family=Source+Sans+3:wght@400;600;700&display=swap">
<style>
  :root {
    --forest: #0a4e27;
    --brand-green: #13994a;
    --sun-yellow: #f5d20f;
    --paper: #ffffff;
    --ink-grey: #6b6b6b;
    --rule: #c9c9c9;
    --night: #000000;
  }
  * { margin: 0; padding: 0; box-sizing: border-box; }
  html, body {
    width: 1029px; height: 1200px; overflow: hidden;
    background: var(--forest);
    font-family: "Source Sans 3", sans-serif;
  }
  .card {
    position: absolute; left: 187px; width: 677px; height: 397px;
    border-radius: 34px; overflow: hidden;
  }
  .card--front { top: 176px; background: var(--paper); }
  .card--back { top: 611px; background: var(--night); }

  .front-brand {
    position: absolute; left: 50px; top: 92px; width: 220px;
    display: flex; flex-direction: column; align-items: center; gap: 14px;
  }
  .brand-dot { width: 120px; height: 120px; border-radius: 50%; background: var(--sun-yellow); }
  .front-brand .brand-name {
    color: var(--brand-green); font-weight: 600; font-size: 22px; white-space: nowrap;
  }
  .divider {
    position: absolute; left: 302px; top: 73px; width: 1px; height: 231px;
    background: var(--rule);
  }
  .contact { position: absolute; left: 343px; top: 114px; right: 24px; }
  .contact .person {
    color: var(--brand-green); font-weight: 600; font-size: 30px; line-height: 1;
    margin-bottom: 26px;
  }
  .contact .line {
    display: flex; align-items: center; gap: 8px;
    color: var(--ink-grey); font-size: 21px; line-height: 29px; white-space: nowrap;
  }
  .contact .line svg { width: 16px; height: 16px; flex: none; }
  .tagline {
    position: absolute; left: 0; right: 0; top: 322px; text-align: center;
    color: var(--brand-green); font-weight: 600; font-size: 26px;
  }

  .back-brand {
    position: absolute; left: 0; right: 0; top: 140px;
    display: flex; justify-content: center; align-items: center; gap: 16px;
  }
  .back-brand .brand-dot { width: 54px; height: 54px; }
  .back-brand .brand-name {
    color: var(--brand-green); font-weight: 700; font-size: 54px; line-height: 1;
  }
  .back-phone {
    position: absolute; left: 0; right: 0; top: 274px;
    display: flex; justify-content: center; align-items: center; gap: 10px;
    color: var(--brand-green); font-weight: 600; font-size: 30px;
  }
  .back-phone svg { width: 23px; height: 23px; }
  .back-tagline {
    position: absolute; left: 0; right: 0; top: 320px; text-align: center;
    color: var(--sun-yellow); font-weight: 600; font-size: 23px;
  }
</style>
</head>
<body>
  <section class="card card--front">
    <div class="front-brand">
      <span class="brand-dot"></span>
      <span class="brand-name">Brantley Lawn Care</span>
    </div>
    <div class="divider"></div>
    <div class="contact">
      <p class="person">Dexter</p>
      <p class="line">
        <svg viewBox="0 0 24 24" aria-hidden="true"><path fill="var(--sun-yellow)" d="M6.6 10.8a15.1 15.1 0 0 0 6.6 6.6l2.2-2.2a1 1 0 0 1 1-.25 11.4 11.4 0 0 0 3.6.57 1 1 0 0 1 1 1V20a1 1 0 0 1-1 1A17 17 0 0 1 3 4a1 1 0 0 1 1-1h3.5a1 1 0 0 1 1 1c0 1.25.2 2.45.57 3.57a1 1 0 0 1-.25 1z"/></svg>
        555-612-4470
      </p>
      <p class="line">
        <svg viewBox="0 0 24 24" aria-hidden="true"><rect x="2" y="5" width="20" height="14" fill="var(--sun-yellow)"/><path d="M2 5l10 8 10-8M2 19l7-7M22 19l-7-7" stroke="#fff" stroke-width="1.6" fill="none"/></svg>
        tidymow47@quillmail.example
      </p>
    </div>
    <p class="tagline">I am your lawns best friend</p>
  </section>

  <section class="card card--back">
    <div class="back-brand">
      <span class="brand-dot"></span>
      <span class="brand-name">Brantley Lawn Care</span>
    </div>
    <p class="back-phone">
      <svg viewBox="0 0 24 24" aria-hidden="true"><path fill="var(--sun-yellow)" d="M6.6 10.8a15.1 15.1 0 0 0 6.6 6.6l2.2-2.2a1 1 0 0 1 1-.25 11.4 11.4 0 0 0 3.6.57 1 1 0 0 1 1 1V20a1 1 0 0 1-1 1A17 17 0 0 1 3 4a1 1 0 0 1 1-1h3.5a1 1 0 0 1 1 1c0 1.25.2 2.45.57 3.57a1 1 0 0 1-.25 1z"/></svg>
      555-612-4470
    </p>
    <p class="back-tagline">Dependable and Professional</p>
  </section>
</body>
</html>
```